CGSI application splash screen

We need a 1024x768 image for use as an application splash screen.
The image will be displayed full screen on an 10 inch industrial PC 1024x768 screen while our application is launching. The image should convey that the application is "Waiting for connection to Wi-Fi access point..." and include a graphic of the industrial PC connected to the access point via an Ethernet cable. A list of troubleshooting steps should be included at the bottom of the image. The troubleshooting steps should not be the main focus of the image and should be shown in a smaller font (but still readable at 1024x768 displayed on a 10 inch screen).
I will include a mock up of the general idea of what we are looking for as well as image files for the industrial PC, a screenshot of our application to show on the PC's screen and the AP.
For general look and feel and a sense of corporate branding please review our website https://copperlanegrowingsystems.com/. The splash screen should reflect corporate branding.
Users of our application
Agriculture

```html
<!DOCTYPE html>
<html lang="en">
<head>
<meta charset="utf-8">
<title>CGSI splash screen – design options</title>
<link href="https://fonts.googleapis.com/css2?family=Roboto:wght@400;500;700&family=Roboto+Condensed:wght@700&display=swap" rel="stylesheet">
<style>
:root{
  --board:#8a8a8a;
  --board-light:#a9a9a9;
  --label:#f5c518;
  --green:#2a9245;
  --green-dark:#1b6e32;
  --green-soft:#8fc99a;
  --ink:#1d1d1d;
  --white:#ffffff;
  --field:#6f9a4a;
  --field-dark:#4d7430;
  --sky:#9cc6ea;
}
*{margin:0;padding:0;box-sizing:border-box}
html,body{width:1200px;height:331px;overflow:hidden}
body{background:linear-gradient(180deg,var(--board) 0%,var(--board-light) 100%);font-family:'Roboto',sans-serif;position:relative}
.option-label{position:absolute;top:9px;font-family:'Roboto',sans-serif;font-size:16px;letter-spacing:1px;color:var(--label)}
.splash{position:absolute;top:31px;width:358px;height:268px;background:var(--white);overflow:hidden}
.backdrop{position:absolute;inset:0}
.splash--faded .backdrop{top:95px;height:110px;background:linear-gradient(180deg,rgba(255,255,255,1) 0%,rgba(190,210,170,.55) 40%,rgba(160,190,130,.45) 70%,rgba(255,255,255,1) 100%)}
.splash--field .backdrop{background:linear-gradient(180deg,#fbfbfb 0%,#f4f6f4 32%,var(--sky) 48%,#b9d59a 58%,var(--field) 72%,var(--field-dark) 100%)}
.splash--scenic .backdrop{background:linear-gradient(180deg,#8fbde6 0%,#c9def0 14%,#7aa155 28%,var(--field) 50%,#c2a878 66%,rgba(255,255,255,.9) 74%,#fff 78%)}
.brand{position:absolute;top:11px;left:0;right:0;text-align:center;color:var(--ink)}
.brand-name{display:inline-flex;align-items:center;gap:4px;font-weight:700;font-size:27px;line-height:27px;letter-spacing:1px}
.brand-dot{width:14px;height:14px;border-radius:50%;background:var(--green)}
.brand-full{font-size:8px;font-weight:700;margin-top:2px}
.headline{position:absolute;top:61px;left:0;width:358px;text-align:center}
.headline-main{font-family:'Roboto Condensed',sans-serif;font-weight:700;font-size:20px;color:var(--green);line-height:21px}
.headline-sub{font-size:14px;font-weight:500;color:var(--ink);line-height:17px}
.splash--scenic .headline-main{color:var(--green-dark);text-shadow:0 0 2px #fff,0 0 3px #fff,0 0 4px #fff,0 0 6px #fff,0 0 8px #fff}
.splash--scenic .headline-sub{color:#000;text-shadow:0 0 2px #fff,0 0 3px #fff,0 0 5px #fff,0 0 7px #fff}
.diagram{position:absolute;inset:0}
.device-label{position:absolute;font-size:5.6px;font-weight:500;color:var(--ink);white-space:nowrap}
.device-label small{display:block;font-size:4.2px;font-weight:700;text-align:center}
.splash--field .device-label{color:var(--white);text-shadow:0 0 2px #1f5a20,0 0 3px #1f5a20}
.band{position:absolute;left:0;right:0;bottom:0;height:64px;background:var(--green)}
.steps{position:absolute;left:61px;top:8px;width:225px;color:var(--white);font-size:4.2px;line-height:6.4px}
.steps h2{font-size:5.4px;font-weight:700;line-height:7px}
.steps ul{list-style:disc;padding-left:6px}
.steps ul ul{padding-left:11px}
</style>
</head>
<body>

<div class="option-label" style="left:294px">option 1</div>
<div class="option-label" style="left:678px">option 2</div>
<div class="option-label" style="left:1066px">option 3</div>

<section class="splash splash--faded" style="left:36px">
  <div class="backdrop" role="img" aria-label="Faded photo of green crop rows in a field"></div>
  <div class="brand"><div class="brand-name"><span class="brand-dot"></span>CGSI</div><div class="brand-full">Copper Lane Growing Systems Inc.</div></div>
  <div class="headline"><div class="headline-main">Waiting for connection</div><div class="headline-sub">to Wi-Fi access point...</div></div>
  <svg class="diagram" viewBox="0 0 358 268" width="358" height="268">
    <line x1="137" y1="145" x2="300" y2="145" stroke="var(--green)" stroke-width="2"/>
    <rect x="28" y="101" width="109" height="85" rx="6" fill="#2a2a2a" role="img" aria-label="Photo of the rugged tractor cab computer showing the seeding app"/>
    <rect x="38" y="109" width="89" height="63" fill="#dfe6e0"/>
    <circle cx="199" cy="145" r="16" fill="var(--white)"/><circle cx="199" cy="145" r="13" fill="var(--green)"/>
    <rect x="192" y="139" width="14" height="11" rx="2" fill="none" stroke="#fff" stroke-width="1.6"/><rect x="196" y="143" width="6" height="3" fill="#fff"/>
    <rect x="296" y="60" width="16" height="125" rx="4" fill="#e6e8e8" role="img" aria-label="Photo of the outdoor Wi-Fi access point with two antennas"/>
  </svg>
  <div class="device-label" style="left:181px;top:165px">Ethernet cable</div>
  <div class="device-label" style="left:51px;top:190px">Tractor cab computer</div>
  <div class="device-label" style="left:282px;top:188px">Wi-Fi access point<small>Netwave AX-200 Outdoor</small></div>
  <div class="band">
    <svg width="358" height="64" viewBox="0 0 358 64" style="position:absolute;inset:0">
      <rect x="14" y="8" width="40" height="46" rx="14" fill="var(--green-soft)" role="img" aria-label="Soft green decorative shape"/>
      <polygon points="283,64 345,0 358,0 358,10 308,64" fill="var(--green-soft)"/>
      <polygon points="315,64 358,18 358,27 323,64" fill="var(--white)"/>
    </svg>
    <div class="steps"><h2>Troubleshooting steps:</h2><ul><li>This screen should only be visible for a short time on boot.</li><li>If this screen stays visible for more than a minute:<ul><li>Verify that the Wi-Fi Access Point (AP) powers up when this system does (indicated by a green light on the side of the AP).</li><li>Check the Ethernet cable between this system and the AP for damage, and replace it if necessary.</li><li>Power-cycle this system and wait for it to reboot fully.</li><li>If the issue persists, contact CGSI support for further assistance.</li></ul></li></ul></div>
  </div>
</section>

<section class="splash splash--field" style="left:421px">
  <div class="backdrop" role="img" aria-label="Photo of crop rows in a field under a blue sky"></div>
  <div class="brand"><div class="brand-name"><span class="brand-dot"></span>CGSI</div><div class="brand-full">Copper Lane Growing Systems Inc.</div></div>
  <div class="headline"><div class="headline-main">Waiting for connection</div><div class="headline-sub">to Wi-Fi access point...</div></div>
  <svg class="diagram" viewBox="0 0 358 268" width="358" height="268">
    <line x1="137" y1="145" x2="300" y2="145" stroke="var(--green)" stroke-width="2"/>
    <rect x="28" y="101" width="109" height="85" rx="6" fill="#2a2a2a" role="img" aria-label="Photo of the rugged tractor cab computer showing the seeding app"/>
    <rect x="38" y="109" width="89" height="63" fill="#dfe6e0"/>
    <circle cx="199" cy="145" r="16" fill="var(--white)"/><circle cx="199" cy="145" r="13" fill="var(--green)"/>
    <rect x="192" y="139" width="14" height="11" rx="2" fill="none" stroke="#fff" stroke-width="1.6"/><rect x="196" y="143" width="6" height="3" fill="#fff"/>
    <rect x="296" y="60" width="16" height="125" rx="4" fill="#e6e8e8" role="img" aria-label="Photo of the outdoor Wi-Fi access point with two antennas"/>
  </svg>
  <div class="device-label" style="left:181px;top:165px">Ethernet cable</div>
  <div class="device-label" style="left:51px;top:190px">Tractor cab computer</div>
  <div class="device-label" style="left:282px;top:188px">Wi-Fi access point<small>Netwave AX-200 Outdoor</small></div>
  <div class="band">
    <svg width="358" height="64" viewBox="0 0 358 64" style="position:absolute;inset:0">
      <rect x="14" y="8" width="40" height="46" rx="14" fill="var(--green-soft)" role="img" aria-label="Soft green decorative shape"/>
      <polygon points="283,64 345,0 358,0 358,10 308,64" fill="var(--green-soft)"/>
      <polygon points="315,64 358,18 358,27 323,64" fill="var(--field-dark)"/>
    </svg>
    <div class="steps"><h2>Troubleshooting steps:</h2><ul><li>This screen should only be visible for a short time on boot.</li><li>If this screen stays visible for more than a minute:<ul><li>Verify that the Wi-Fi Access Point (AP) powers up when this system does (indicated by a green light on the side of the AP).</li><li>Check the Ethernet cable between this system and the AP for damage, and replace it if necessary.</li><li>Power-cycle this system and wait for it to reboot fully.</li><li>If the issue persists, contact CGSI support for further assistance.</li></ul></li></ul></div>
  </div>
</section>

<section class="splash splash--scenic" style="left:805px">
  <div class="backdrop" role="img" aria-label="Photo of a flowering potato field with trees and sky"></div>
  <div class="brand"><div class="brand-name"><span class="brand-dot"></span>CGSI</div><div class="brand-full">Copper Lane Growing Systems Inc.</div></div>
  <div class="headline"><div class="headline-main">Waiting for connection</div><div class="headline-sub">to Wi-Fi access point...</div></div>
  <svg class="diagram" viewBox="0 0 358 268" width="358" height="268">
    <line x1="137" y1="145" x2="300" y2="145" stroke="var(--white)" stroke-width="2"/>
    <rect x="28" y="101" width="109" height="85" rx="6" fill="#2a2a2a" role="img" aria-label="Photo of the rugged tractor cab computer showing the seeding app"/>
    <rect x="38" y="109" width="89" height="63" fill="#dfe6e0"/>
    <circle cx="199" cy="145" r="16" fill="var(--white)"/><circle cx="199" cy="145" r="13" fill="var(--green)"/>
    <rect x="192" y="139" width="14" height="11" rx="2" fill="none" stroke="#fff" stroke-width="1.6"/><rect x="196" y="143" width="6" height="3" fill="#fff"/>
    <rect x="296" y="60" width="16" height="125" rx="4" fill="#eceeee" role="img" aria-label="Photo of the outdoor Wi-Fi access point with two antennas"/>
  </svg>
  <div class="device-label" style="left:181px;top:165px">Ethernet cable</div>
  <div class="device-label" style="left:51px;top:190px">Tractor cab computer</div>
  <div class="device-label" style="left:282px;top:188px">Wi-Fi access point<small>Netwave AX-200 Outdoor</small></div>
  <div class="band">
    <svg width="358" height="64" viewBox="0 0 358 64" style="position:absolute;inset:0">
      <rect x="14" y="8" width="40" height="46" rx="14" fill="var(--green-soft)" role="img" aria-label="Soft green decorative shape"/>
      <polygon points="283,64 345,0 358,0 358,10 308,64" fill="var(--green-soft)"/>
      <polygon points="315,64 358,18 358,27 323,64" fill="var(--white)"/>
    </svg>
    <div class="steps"><h2>Troubleshooting steps:</h2><ul><li>This screen should only be visible for a short time on boot.</li><li>If this screen stays visible for more than a minute:<ul><li>Verify that the Wi-Fi Access Point (AP) powers up when this system does (indicated by a green light on the side of the AP).</li><li>Check the Ethernet cable between this system and the AP for damage, and replace it if necessary.</li><li>Power-cycle this system and wait for it to reboot fully.</li><li>If the issue persists, contact CGSI support for further assistance.</li></ul></li></ul></div>
  </div>
</section>

</body>
</html>
```